GIF Dynamic for Marketing Agency

Need a Dynamic GIF Created for Web Banner Placement. This is to Promote the Company, It's Products and Services on a Web Directory. Needs to contain a Creative Button/Call to Action such as 'Get Leads'

About the Company: Company is a Lead Generation Company Servicing Business Finance Professionals. Company Provides the Following Primary Products and Services:

-Lead Generation
-Live Calls
-Appointments
-Ads Management
-Aged Leads
-B2B Data
(2) Sizes: 250x250(Desktop) & 728 x 90 (Mobile)

*RECOMMENDED. Visit Company Website (See Logo) to Understand its Products & Services to develop insights as to what the company is looking for.

Target Market(s)

Business Loan Brokers

Industry/Entity Type

Marketing

Colors
0054AA
0677BA
7BADD7
CADEEF
E8F1F8
0094D4
00A9DD
6FCCEA
C7EBF8
E9F6FB
FFF300
FFF600
FEFA6F
FFFEC7
FFFEE8
EE7325
F08F49
F5BC92
FAE3D3
FDF4ED

Requirements
Must have
• Dynamic GIF. 2 Sizes. 250x250 & 728x90. CREATIVITY. Call to Action. Unique, Professional & Modern.
Nice to have
• Colorful
Should not have
• No Clipart Whatsoever.

```html
<!DOCTYPE html>
<html lang="en">
<head>
<meta charset="utf-8">
<title>Get Leads – Web Banners</title>
<link rel="stylesheet" href="https://fonts.googleapis.com/css2?family=Montserrat:ital,wght@1,900&display=swap">
<style>
  :root {
    --page-bg: #f3f7fc;
    --blue-deep: #4656f6;
    --blue-mid: #3b8cf8;
    --blue-cyan: #0be6f9;
    --shape-blue: #2b45ee;
    --dot-dark: #2a3fe0;
    --orange-light: #ffbf2a;
    --orange: #ffa812;
    --orange-dark: #f49400;
    --badge-red: #ff4f18;
    --badge-orange: #ff8a12;
    --text-white: #ffffff;
    --text-lavender: #d9dcf4;
  }
  html, body {
    margin: 0;
    padding: 0;
    width: 1200px;
    height: 704px;
    overflow: hidden;
    background: var(--page-bg);
  }
  .banner {
    position: absolute;
    display: block;
    box-shadow: 0 6px 18px rgba(40, 70, 140, 0.12);
  }
  .banner--square { left: 390px; top: 46px; width: 422px; height: 422px; }
  .banner--leaderboard { left: 42px; top: 512px; width: 1117px; height: 138px; }
  .cta-word {
    font-family: "Montserrat", Arial, sans-serif;
    font-weight: 900;
    font-style: italic;
    letter-spacing: -2px;
  }
  .deco-shape { fill: var(--shape-blue); opacity: 0.45; }
  .deco-dot { fill: var(--dot-dark); opacity: 0.55; }
</style>
</head>
<body>

<svg class="banner banner--square" viewBox="0 0 528 528" role="img" aria-label="Get Leads square banner">
  <defs>
    <linearGradient id="sq-bg" x1="0" y1="1" x2="1" y2="0">
      <stop offset="0" stop-color="var(--blue-deep)"/>
      <stop offset="0.55" stop-color="var(--blue-mid)"/>
      <stop offset="1" stop-color="var(--blue-cyan)"/>
    </linearGradient>
    <linearGradient id="pill-fill" x1="0" y1="0" x2="1" y2="1">
      <stop offset="0" stop-color="var(--orange-light)"/>
      <stop offset="0.5" stop-color="var(--orange)"/>
      <stop offset="1" stop-color="var(--orange-dark)"/>
    </linearGradient>
    <linearGradient id="word-fill" x1="0" y1="0" x2="0" y2="1">
      <stop offset="0" stop-color="var(--text-white)"/>
      <stop offset="1" stop-color="var(--text-lavender)"/>
    </linearGradient>
    <linearGradient id="badge-fill" x1="0" y1="1" x2="1" y2="0">
      <stop offset="0" stop-color="var(--badge-red)"/>
      <stop offset="1" stop-color="var(--badge-orange)"/>
    </linearGradient>
    <radialGradient id="coin-fill" cx="0.4" cy="0.4" r="0.6">
      <stop offset="0" stop-color="#ffd23a"/>
      <stop offset="1" stop-color="var(--orange-dark)"/>
    </radialGradient>
    <filter id="sq-pill-shadow" x="-20%" y="-30%" width="140%" height="170%">
      <feDropShadow dx="0" dy="8" stdDeviation="6" flood-color="#1a2a90" flood-opacity="0.35"/>
    </filter>
    <filter id="sq-word-shadow" x="-10%" y="-20%" width="130%" height="150%">
      <feDropShadow dx="4" dy="6" stdDeviation="3" flood-color="#b35d00" flood-opacity="0.55"/>
    </filter>
  </defs>

  <rect class="backdrop" width="528" height="528" fill="url(#sq-bg)"/>

  <g class="deco">
    <rect class="deco-shape" x="303" y="53" width="230" height="55" rx="27"/>
    <rect class="deco-shape" x="193" y="93" width="260" height="120" rx="60"/>
    <rect class="deco-shape" x="33" y="238" width="220" height="110" rx="55"/>
    <rect class="deco-shape" x="233" y="373" width="270" height="120" rx="60"/>
    <circle class="deco-dot" cx="59" cy="70" r="9"/>
    <circle class="deco-dot" cx="213" cy="461" r="9"/>
    <circle class="deco-dot" cx="288" cy="78" r="6"/>
    <circle class="coin" cx="90" cy="120" r="27" fill="url(#coin-fill)"/>
    <circle class="coin" cx="439" cy="241" r="13" fill="url(#coin-fill)"/>
    <circle class="coin" cx="331" cy="460" r="24" fill="url(#coin-fill)"/>
  </g>

  <g class="cta-pill" transform="translate(256 200) rotate(-7)">
    <rect x="-165" y="-72" width="330" height="144" rx="72" fill="url(#pill-fill)" filter="url(#sq-pill-shadow)"/>
    <text class="cta-word" x="0" y="38" font-size="108" text-anchor="middle" fill="url(#word-fill)" filter="url(#sq-word-shadow)">GET</text>
  </g>

  <g class="cta-pill" transform="translate(261 353) rotate(-7)">
    <rect x="-250" y="-75" width="500" height="150" rx="75" fill="url(#pill-fill)" filter="url(#sq-pill-shadow)"/>
    <text class="cta-word" x="0" y="40" font-size="114" text-anchor="middle" fill="url(#word-fill)" filter="url(#sq-word-shadow)">LEADS</text>
  </g>

  <g class="send-badge" transform="translate(447 86)">
    <circle r="55" fill="url(#badge-fill)"/>
    <polygon points="-41,-3 26,-33 11,39 -3,9" fill="var(--text-white)"/>
  </g>
</svg>

<svg class="banner banner--leaderboard" viewBox="0 0 1396 173" preserveAspectRatio="none" role="img" aria-label="Get Leads leaderboard banner">
  <defs>
    <linearGradient id="lb-bg" x1="0" y1="1" x2="1" y2="0">
      <stop offset="0" stop-color="var(--blue-deep)"/>
      <stop offset="0.6" stop-color="var(--blue-mid)"/>
      <stop offset="1" stop-color="var(--blue-cyan)"/>
    </linearGradient>
    <filter id="lb-pill-shadow" x="-10%" y="-20%" width="120%" height="150%">
      <feDropShadow dx="0" dy="5" stdDeviation="5" flood-color="#1a2a90" flood-opacity="0.35"/>
    </filter>
    <filter id="lb-word-shadow" x="-10%" y="-20%" width="130%" height="150%">
      <feDropShadow dx="4" dy="6" stdDeviation="3" flood-color="#b35d00" flood-opacity="0.55"/>
    </filter>
  </defs>

  <rect class="backdrop" width="1396" height="173" fill="url(#lb-bg)"/>

  <g class="deco">
    <rect class="deco-shape" x="32" y="35" width="95" height="45" rx="22"/>
    <rect class="deco-shape" x="52" y="55" width="260" height="110" rx="55"/>
    <rect class="deco-shape" x="540" y="70" width="160" height="80" rx="40"/>
    <rect class="deco-shape" x="1232" y="78" width="80" height="35" rx="17"/>
    <rect class="deco-shape" x="1147" y="95" width="150" height="70" rx="35"/>
    <circle class="deco-dot" cx="27" cy="147" r="16"/>
    <circle class="deco-dot" cx="10" cy="10" r="4"/>
    <circle class="deco-dot" cx="1380" cy="160" r="4"/>
    <circle class="deco-dot" cx="1372" cy="22" r="4"/>
    <circle class="coin" cx="136" cy="31" r="12" fill="url(#coin-fill)"/>
    <circle class="coin" cx="1360" cy="90" r="17" fill="url(#coin-fill)"/>
    <circle class="coin" cx="1118" cy="153" r="11" fill="url(#coin-fill)"/>
  </g>

  <g class="cta-pill">
    <rect x="169" y="10" width="361" height="153" rx="76" fill="url(#pill-fill)" filter="url(#lb-pill-shadow)"/>
    <text class="cta-word" x="350" y="130" font-size="120" text-anchor="middle" fill="url(#word-fill)" filter="url(#lb-word-shadow)">GET</text>
  </g>

  <g class="cta-pill">
    <rect x="562" y="10" width="550" height="153" rx="76" fill="url(#pill-fill)" filter="url(#lb-pill-shadow)"/>
    <text class="cta-word" x="837" y="130" font-size="122" text-anchor="middle" fill="url(#word-fill)" filter="url(#lb-word-shadow)">LEADS</text>
  </g>

  <g class="send-badge" transform="translate(1178 62)">
    <circle r="50" fill="url(#badge-fill)"/>
    <polygon points="-37,-3 24,-30 10,35 -3,8" fill="var(--text-white)"/>
  </g>
</svg>

</body>
</html>
```